Upcoming lecture sponsored by a church on an important topic

We have a Reformation The Speech coming up at the end of October on the topic of law and gospel. I thought it might be cool to use a flyer that looks like it was from that day and age. Picture what Conrad Velmer would advertise things on kind of an old church/reformation type format. It will be sponsored by our church, and we have a paragraph or two to describe the lecture that would be included on the flyer. We would also want it formatted so that it could be printed on postcards and mailed to churches and individuals.

The flyer should have the following paragraph...

The distinction between the law and the gospel is the most important distinction in the Christian faith. Conrad Velmer: “Distinguishing between the law and the gospel is the highest art in Christendom, one who every person who values the name Christian ought to recognize, know, and possess.” The distinction between the law and the gospel is of great comfort for the child of God. “For the law was given by Moses, but grace and truth came by Jesus Christ” (John 1:17). For these reasons, the distinction between the law and the gospel is the most heavily assaulted doctrine in the Christian faith. This Reformation Day, join us for an explanation and defense of the great distinction between God’s good law and God’s glorious gospel.

And the flyer should have the following information...

Topic: The Steady Word and the Bright Promise
Date and Time: Tuesday, October 31, 2023 at 7:30pm
Host: Harrow Creek Fellowship Church
Speaker: Rev. Gerald Voskuil
Venue: The Marlow Hall, 5172 Brenton Avenue, Alder Falls, OR 49318
Format: Lecture followed by Q&A and refreshments

00AB8E
00BBA5
67D7C9
C6EFE9
E9F9F6

• The color scheme that I would like to have is a teal color (the same color as found at www.brackenhollowchapel.com

```html
<!DOCTYPE html>
<html lang="en">
<head>
<meta charset="utf-8">
<title>Reformation Day Lecture – Flyer and Postcard</title>
<link rel="stylesheet" href="https://fonts.googleapis.com/css2?family=Cinzel:wght@400;600&family=Poppins:wght@300;400;500&display=swap">
<style>
  :root{
    --backdrop:#a8b1bb;
    --paper:#ebebeb;
    --white:#ffffff;
    --teal:#3a9aa5;
    --teal-deep:#1f5560;
    --ink:#1f1f1f;
    --body-ink:#1f5560;
  }
  *{margin:0;padding:0;box-sizing:border-box}
  html,body{width:1200px;height:2803px;overflow:hidden;background:var(--backdrop)}
  body{position:relative;font-family:"Poppins",sans-serif}
  .sheet{position:absolute;background:var(--paper);overflow:hidden}
  .band{position:absolute;left:0;right:0;background:var(--white)}
  .frame{position:absolute;border:solid var(--teal)}
  .rule{position:absolute;height:4px;background:var(--teal)}
  .centered{position:absolute;left:0;right:0;text-align:center}
  .kicker{font-family:"Cinzel",serif;font-weight:600;color:var(--teal-deep);letter-spacing:1px}
  .headline{font-family:"Cinzel",serif;font-weight:600;color:var(--teal);line-height:1.07}
  .date{font-weight:400;color:var(--teal);line-height:1.2}
  .copy{position:absolute;color:var(--body-ink);font-weight:400}
  .copy p{text-align:justify;text-align-last:center}
  .tag{position:absolute;background:var(--teal);color:var(--white);font-family:"Cinzel",serif;text-align:center;letter-spacing:1px}
  .detail{position:absolute;text-align:center;color:var(--ink);font-weight:500}

  /* Flyer */
  .flyer{left:96px;top:58px;width:985px;height:1393px}
  .flyer .band{top:209px;height:421px}
  .flyer .frame-outer{left:30px;top:33px;width:923px;height:1191px;border-width:5px}
  .flyer .frame-inner{left:47px;top:55px;width:889px;height:1147px;border-width:2px}
  .flyer .gap{position:absolute;left:327px;top:1195px;width:329px;height:34px;background:var(--paper)}
  .flyer .kicker{top:92px;font-size:46px}
  .flyer .rule{left:153px;width:678px}
  .flyer .headline{top:252px;font-size:72px}
  .flyer .date{top:456px;font-size:38px}
  .flyer .copy{left:100px;width:780px;top:622px;font-size:19.5px;line-height:24px}
  .flyer .copy p{margin-bottom:24px}
  .flyer .tag{width:175px;height:28px;font-size:22px;line-height:29px}
  .flyer .detail{width:260px;font-size:20px;line-height:24px}
  .flyer .venue-line{position:absolute;left:0;right:0;top:1232px;text-align:center;font-size:19.5px;font-weight:500;color:var(--ink)}
  .flyer .web-tab{position:absolute;left:0;top:0}
  .flyer .web-text{position:absolute;left:0;right:0;top:1338px;text-align:center;color:var(--white);font-size:20px;font-weight:500;letter-spacing:3px}

  /* Postcard front */
  .card-front{left:156px;top:1528px;width:865px;height:577px}
  .card-front .band{top:110px;height:180px}
  .card-front .frame-outer{left:36px;top:33px;width:794px;height:515px;border-width:5px}
  .card-front .frame-inner{left:51px;top:48px;width:764px;height:485px;border-width:2px}
  .card-front .kicker{top:56px;font-size:30px}
  .card-front .rule{left:211px;width:444px;height:3px}
  .card-front .headline{top:141px;font-size:40px}
  .card-front .date{top:247px;font-size:23px}
  .card-front .copy{left:89px;width:688px;top:303px;font-size:13.5px;line-height:17px}
  .card-front .copy p{margin-bottom:16px}

  /* Postcard back */
  .card-back{left:156px;top:2160px;width:865px;height:575px}
  .card-back .frame-outer{left:36px;top:28px;width:444px;height:517px;border-width:5px}
  .card-back .frame-inner{left:50px;top:42px;width:416px;height:489px;border-width:2px}
  .card-back .tag{left:152px;width:212px;height:27px;font-size:21px;line-height:28px}
  .card-back .detail{left:58px;width:400px;font-size:20px;line-height:24px}
  .card-back .web-line{position:absolute;left:97px;width:323px;top:488px;border-top:1px solid var(--teal);border-bottom:1px solid var(--teal);height:25px;text-align:center;font-size:16.5px;line-height:23px;color:var(--ink)}
  .card-back .stamp{position:absolute;left:742px;top:28px;width:81px;height:80px;background:var(--white)}
  .card-back .address-line{position:absolute;left:506px;width:317px;border-top:2px dotted #777}
</style>
</head>
<body>

<section class="sheet flyer" aria-label="Lecture flyer">
  <div class="band"></div>
  <div class="frame frame-outer"></div>
  <div class="frame frame-inner"></div>
  <div class="gap"></div>

  <h2 class="centered kicker">REFORMATION DAY LECTURE</h2>
  <div class="rule" style="top:236px"></div>
  <h1 class="centered headline">THE STEADY WORD &amp;<br>THE BRIGHT PROMISE</h1>
  <div class="rule" style="top:418px"></div>
  <p class="centered date">OCTOBER 31, 2023<br>7:30PM</p>

  <div class="copy">
    <p style="padding:0 120px">The distinction between the law and the gospel is the most important distinction in the Christian faith.</p>
    <p>Conrad Velmer: “Distinguishing between the law and the gospel is the highest art in Christendom, one who every person who values the name Christian ought to recognize, know, and possess.”</p>
    <p>The distinction between the law and the gospel is of great comfort for the child of God. “For the law was given by Moses, but grace and truth came by Jesus Christ” (John 1:17).</p>
    <p>For these reasons, the distinction between the law and the gospel is the most heavily assaulted doctrine in the Christian faith. This Reformation Day, join us for an explanation and defense of the great distinction between God’s good law and God’s glorious gospel.</p>
  </div>

  <div class="tag" style="left:118px;top:1055px">HOST</div>
  <div class="detail" style="left:76px;top:1090px">Harrow Creek Fellowship Church</div>
  <div class="tag" style="left:403px;top:1055px">SPEAKER</div>
  <div class="detail" style="left:361px;top:1090px">Rev. Gerald Voskuil</div>
  <div class="tag" style="left:690px;top:1055px">FORMAT</div>
  <div class="detail" style="left:648px;top:1090px">Lecture followed by<br>Q&amp;A and refreshments</div>

  <div class="tag" style="left:403px;top:1196px">VENUE</div>
  <p class="venue-line">The Marlow Hall, 5172 Brenton Avenue, Alder Falls, OR 49318</p>

  <svg class="web-tab" width="985" height="1393" viewBox="0 0 985 1393" aria-hidden="true">
    <path d="M232 1393 C248 1380 250 1327 272 1327 H713 C735 1327 737 1380 753 1393 Z" fill="#3a9aa5"/>
  </svg>
  <p class="web-text">www.harrowcreekfellowship.org</p>
</section>

<section class="sheet card-front" aria-label="Postcard front">
  <div class="band"></div>
  <div class="frame frame-outer"></div>
  <div class="frame frame-inner"></div>
  <h2 class="centered kicker">REFORMATION DAY LECTURE</h2>
  <div class="rule" style="top:131px"></div>
  <h1 class="centered headline">THE STEADY WORD &amp;<br>THE BRIGHT PROMISE</h1>
  <div class="rule" style="top:233px"></div>
  <p class="centered date">OCTOBER 31, 2023 AT 7:30PM</p>
  <div class="copy">
    <p style="padding:0 160px">The distinction between the law and the gospel is the most important distinction in the Christian faith.</p>
    <p>Conrad Velmer: “Distinguishing between the law and the gospel is the highest art in Christendom, one who every person who values the name Christian ought to recognize, know, and possess.”</p>
    <p>The distinction between the law and the gospel is of great comfort for the child of God. “For the law was given by Moses, but grace and truth came by Jesus Christ” (John 1:17).</p>
    <p>For these reasons, the distinction between the law and the gospel is the most heavily assaulted doctrine in the Christian faith. This Reformation Day, join us for an explanation and defense of the great distinction between God’s good law and God’s glorious gospel.</p>
  </div>
</section>

<section class="sheet card-back" aria-label="Postcard back">
  <div class="frame frame-outer"></div>
  <div class="frame frame-inner"></div>
  <div class="tag" style="top:70px">HOST</div>
  <div class="detail" style="top:102px">Harrow Creek Fellowship Church</div>
  <div class="tag" style="top:157px">SPEAKER</div>
  <div class="detail" style="top:190px">Rev. Gerald Voskuil</div>
  <div class="tag" style="top:240px">FORMAT</div>
  <div class="detail" style="top:272px">Lecture followed by<br>Q&amp;A and refreshments</div>
  <div class="tag" style="top:348px">VENUE</div>
  <div class="detail" style="top:380px">The Marlow Hall,<br>5172 Brenton Avenue, Alder Falls,<br>OR 49318</div>
  <div class="web-line">www.harrowcreekfellowship.org</div>
  <div class="stamp"></div>
  <div class="address-line" style="top:204px"></div>
  <div class="address-line" style="top:285px"></div>
  <div class="address-line" style="top:364px"></div>
  <div class="address-line" style="top:444px"></div>
</section>

</body>
</html>
```